un:varnish - book cover design needed

I need a book cover designed for a new book that I'll be publishing shortly.

Title of the books is "un:varnish" and the slogan is "How to get the most out of your people resources!"

The book is a satirical business guide that is aimed at executives, leaders and new managers. Instead of promoting the rampant rehumanisation of business in this new economic era, we are instead encouraging managers to hark back to the good old industrialist notion of viewing your employees as a resource, not as people. Rehumanisation, we argue, has led our businesses astray and explains why productivity and efficiency are so hard to come by. un:varnishing is our answer and in the book we provide leaders with very practical methods on how to embark on a covert programme of un:varnishing.

I need a cover design that is edgy and clever. The book is not for average employees, but only for managers and leaders. It should attract such readers and discourage lowly staff from picking it up. The cover needs to communicate the nature of the satire we write of. It's a business book, but should not look boring.

The authors are "Morton J. Fells with Celia Drummond".

Hi

Thanks for submitting designs so far. 

There are two ideas I'd like to see developed:
1. Checking in your humanity at the reception desk. Like you do with a weapon, bringing in your humanity the workplace is a dangerous thing, so it should be checked in.
2. Employees as assets with asset register stickers. Corporate always catalogue their assets with little bar coded asset registers. I'd like to see some designs that show how your employees are "assetised".

```html
<!DOCTYPE html>
<html lang="en">
<head>
<meta charset="utf-8">
<title>UN:VARNISH — Book Cover</title>
<link rel="stylesheet" href="https://fonts.googleapis.com/css2?family=Oswald:wght@500;600;700&family=Hind:wght@400;500&display=swap">
<style>
  :root {
    --page-bg: #e9e9e9;
    --cover-black: #161616;
    --band-black: #1c1c1c;
    --panel-dark: #0c0c0c;
    --title-white: #f2f2f2;
    --text-grey: #a9a9a9;
    --muted-grey: #8a8a8a;
    --sky-top: #4a5666;
    --sky-blue: #6f8aa6;
    --cloud-grey: #8e8c86;
    --sky-warm: #dccaa0;
    --rock-mid: #6b5444;
    --rock-dark: #2a211b;
  }
  * { box-sizing: border-box; margin: 0; padding: 0; }
  html, body { width: 1200px; height: 800px; overflow: hidden; }
  body {
    background: var(--page-bg);
    font-family: "Hind", sans-serif;
    position: relative;
  }
  .book-wrap {
    position: absolute;
    top: 90px;
    left: 155px;
    display: flex;
    height: 620px;
    box-shadow: 0 12px 30px rgba(0,0,0,0.18);
  }

  /* Back cover */
  .back-cover {
    width: 420px;
    height: 100%;
    background: var(--cover-black);
    padding: 18px 24px 22px;
    display: flex;
    flex-direction: column;
  }
  .back-authors {
    font-family: "Oswald", sans-serif;
    font-weight: 500;
    font-size: 11px;
    letter-spacing: 0.5px;
    color: var(--text-grey);
    text-align: right;
  }
  .back-title {
    font-family: "Oswald", sans-serif;
    font-weight: 700;
    font-size: 62px;
    line-height: 1;
    color: var(--title-white);
    letter-spacing: 1px;
    margin-top: 6px;
  }
  .back-tagline {
    font-family: "Oswald", sans-serif;
    font-weight: 500;
    font-size: 10.5px;
    color: var(--text-grey);
    letter-spacing: 1.4px;
    text-align: center;
    margin-top: 8px;
  }
  .back-blurb {
    margin-top: 14px;
    font-size: 10.5px;
    line-height: 1.45;
    color: var(--text-grey);
    text-align: justify;
  }
  .back-footer {
    margin-top: auto;
    display: flex;
    justify-content: space-between;
  }
  .back-box {
    width: 92px;
    height: 58px;
    background: var(--panel-dark);
    display: flex;
    align-items: center;
    justify-content: center;
    font-size: 9px;
    color: var(--muted-grey);
  }

  /* Spine */
  .spine {
    width: 46px;
    height: 100%;
    background: var(--band-black);
    border-left: 1px solid #2a2a2a;
    border-right: 1px solid #2a2a2a;
    display: flex;
    flex-direction: column;
    align-items: center;
    padding: 14px 0;
  }
  .spine-title, .spine-authors {
    writing-mode: vertical-rl;
    font-family: "Oswald", sans-serif;
    color: var(--title-white);
  }
  .spine-title {
    font-weight: 700;
    font-size: 34px;
    letter-spacing: 1px;
    line-height: 1;
  }
  .spine-authors {
    margin-top: 22px;
    font-weight: 500;
    font-size: 8px;
    letter-spacing: 0.8px;
    color: var(--text-grey);
  }

  /* Front cover */
  .front-cover {
    width: 420px;
    height: 100%;
    background: var(--cover-black);
    display: flex;
    flex-direction: column;
  }
  .front-title-band {
    height: 112px;
    display: flex;
    align-items: center;
    justify-content: center;
  }
  .front-title {
    font-family: "Oswald", sans-serif;
    font-weight: 700;
    font-size: 78px;
    line-height: 1;
    color: var(--title-white);
    letter-spacing: 1px;
  }
  .front-photo {
    position: relative;
    flex: 1;
    background:
      radial-gradient(ellipse 60% 30% at 30% 62%, rgba(220,202,160,0.55), transparent 70%),
      linear-gradient(160deg, transparent 0%, transparent 58%, var(--rock-mid) 66%, var(--rock-dark) 100%),
      radial-gradient(ellipse 45% 22% at 20% 26%, rgba(111,138,166,0.7), transparent 70%),
      radial-gradient(ellipse 60% 35% at 80% 35%, rgba(142,140,134,0.8), transparent 75%),
      linear-gradient(180deg, var(--sky-top) 0%, var(--cloud-grey) 38%, var(--sky-warm) 58%, #9c8a78 66%);
  }
  .front-tagline {
    position: absolute;
    top: 22px;
    left: 0;
    right: 0;
    text-align: center;
    font-family: "Oswald", sans-serif;
    font-weight: 600;
    font-size: 24px;
    line-height: 1.15;
    color: var(--title-white);
    text-shadow: 0 0 3px #000, 1px 1px 2px #000;
  }
  .front-author-band {
    height: 40px;
    display: flex;
    align-items: center;
    justify-content: center;
    font-family: "Oswald", sans-serif;
    font-weight: 600;
    font-size: 12px;
    letter-spacing: 0.8px;
    color: var(--title-white);
  }
</style>
</head>
<body>
  <div class="book-wrap">
    <section class="back-cover">
      <p class="back-authors">BY: MORTON J. FELLS WITH CELIA DRUMMOND</p>
      <h2 class="back-title">UN:VARNISH</h2>
      <p class="back-tagline">HOW TO GET THE MOST OUT OF YOUR PEOPLE RESOURCES!</p>
      <p class="back-blurb">Lorem ipsum dolor sit amet, consectetur adipisicing elit, sed do eiusmod tempor incididunt ut labore et dolore magna aliqua. Ut enim ad minim veniam, quis nostrud exercitation. Lorem ipsum dolor sit amet, consectetur adipisicing elit, sed do eiusmod tempor incididunt ut labore et dolore magna aliqua. Ut enim ad minim veniam, quis nostrud exercitation. Lorem ipsum dolor sit amet, consectetur adipisicing elit, sed do eiusmod tempor incididunt ut labore et dolore magna aliqua. Ut enim ad minim veniam, quis nostrud exercitation. Lorem ipsum dolor sit amet, consectetur adipisicing elit, sed do eiusmod tempor incididunt ut labore et dolore magna aliqua. Ut enim ad minim veniam, quis nostrud exercitation. Lorem ipsum dolor sit amet, consectetur adipisicing elit, sed do eiusmod tempor incididunt ut labore et dolore magna aliqua. Ut enim ad minim veniam, quis nostrud exercitation. Lorem ipsum dolor sit amet, consectetur adipisicing elit, sed do eiusmod tempor incididunt ut labore et dolore magna aliqua. Ut enim ad minim veniam, quis nostrud exercitation. Lorem ipsum dolor sit amet, consectetur adipisicing elit, sed do eiusmod tempor incididunt ut labore et dolore magna aliqua. Ut enim ad minim veniam, quis nostrud exercitation. Lorem ipsum dolor sit amet, consectetur adipisicing elit, sed do eiusmod tempor incididunt ut labore et dolore magna aliqua. Ut enim ad minim veniam, quis nostrud exercitation. Lorem ipsum dolor sit amet, consectetur adipisicing elit, sed do eiusmod tempor incididunt ut labore et dolore magna aliqua. Ut enim ad minim veniam, quis nostrud exercitation.</p>
      <div class="back-footer">
        <div class="back-box">LOGO</div>
        <div class="back-box">ISBN</div>
      </div>
    </section>

    <aside class="spine">
      <span class="spine-title">UN:VARNISH</span>
      <span class="spine-authors">MORTON J. FELLS WITH CELIA DRUMMOND</span>
    </aside>

    <section class="front-cover">
      <header class="front-title-band">
        <h1 class="front-title">UN:VARNISH</h1>
      </header>
      <div class="front-photo" role="img" aria-label="Satirical cover photo: on a rocky hilltop under a stormy sky, a businesswoman in a grey suit strains at a rope in a tug-of-war, while the manager at the other end lounges in an office chair and lets her do all the pulling — staff treated as a resource to be worked">
        <p class="front-tagline">HOW TO GET THE MOST<br>OUT OF YOUR PEOPLE RESOURCES!</p>
      </div>
      <footer class="front-author-band">BY: MORTON J. FELLS WITH CELIA DRUMMOND</footer>
    </section>
  </div>
</body>
</html>
```